Logo and business card for optometric practice
Curtis Hallorann & Associates
Marta Pelovska, O.D.
Oscar Tremwitz, O.D.
Neil Borromi, O.D.
417 Pembrook Parkway
Brantwell Harbor, Vermont 05871
516-902-4471

Target Market(s)

Patients, general public

Industry/Entity Type

Business

Logo Text

Curtis Hallorann & Associates Optometrists

Logo styles of interest
Pictorial/Combination Logo
Font styles to use
Serif
Sans Serif

Requirements
Must have
• current inspiration: realistic or photo closeup of eye, with interesting treatment of the iris OR
tech look, with closeup of eye and grid like the doctor is looking through a camera or microscope to view the eye up close
Should not have
• NO cartoons

```html
<!DOCTYPE html>
<html lang="en">
<head>
<meta charset="utf-8">
<title>Curtis Hallorann &amp; Associates – Business Card</title>
<link rel="stylesheet" href="https://fonts.googleapis.com/css2?family=Arimo:wght@400;700&display=swap">
<style>
  :root {
    --page-bg: #ffffff;
    --card-bg: #ffffff;
    --brand-blue: #1d3a94;
    --wave-blue: #0e538f;
    --wave-teal: #18767f;
    --wave-green: #249c78;
    --mark-blue: #1d5a9c;
    --text-light: #ffffff;
  }
  * { margin: 0; padding: 0; box-sizing: border-box; }
  html, body {
    width: 1200px;
    height: 990px;
    overflow: hidden;
    background: var(--page-bg);
  }
  .card {
    position: absolute;
    left: 20px;
    top: 155px;
    width: 1162px;
    height: 665px;
    background: var(--card-bg);
    box-shadow: 0 2px 8px rgba(0, 0, 0, 0.18);
    overflow: hidden;
    font-family: "Arimo", Arial, sans-serif;
  }
  .card__wave {
    position: absolute;
    left: 0;
    top: 0;
    width: 1162px;
    height: 665px;
  }
  .brand {
    position: absolute;
    left: 0;
    top: 44px;
    width: 1170px;
    text-align: center;
    color: var(--brand-blue);
    font-weight: 400;
  }
  .brand__dot {
    display: block;
    width: 124px;
    height: 124px;
    margin: 0 auto 52px;
    border-radius: 50%;
    background: var(--mark-blue);
  }
  .brand__name {
    font-size: 40px;
    line-height: 50px;
  }
  .brand__rule {
    display: block;
    width: 303px;
    height: 2px;
    margin: 1px auto 0;
    background: var(--brand-blue);
  }
  .brand__trade {
    margin-top: 13px;
    font-size: 45px;
    line-height: 48px;
    letter-spacing: 1.5px;
  }
  .doctors, .contact {
    position: absolute;
    color: var(--text-light);
    font-weight: 700;
    font-size: 34px;
    line-height: 42px;
    list-style: none;
  }
  .doctors { left: 44px; top: 496px; }
  .contact { left: 580px; top: 502px; font-style: normal; }
</style>
</head>
<body>
  <main class="card">
    <svg class="card__wave" viewBox="0 0 1162 665" aria-hidden="true">
      <defs>
        <linearGradient id="waveGradient" x1="0" y1="0" x2="1" y2="0">
          <stop offset="0" stop-color="var(--wave-blue)"/>
          <stop offset="0.5" stop-color="var(--wave-teal)"/>
          <stop offset="1" stop-color="var(--wave-green)"/>
        </linearGradient>
      </defs>
      <path d="M0,307 C50,285 120,276 210,288 C380,315 510,455 630,482 C820,520 1040,420 1162,333 L1162,665 L0,665 Z" fill="url(#waveGradient)"/>
    </svg>

    <header class="brand">
      <span class="brand__dot" aria-hidden="true"></span>
      <p class="brand__name">Curtis Hallorann<br>&amp; Associates</p>
      <span class="brand__rule" aria-hidden="true"></span>
      <p class="brand__trade">OPTOMETRISTS</p>
    </header>

    <ul class="doctors">
      <li>Marta Pelovska, O.D.</li>
      <li>Oscar Tremwitz, O.D.</li>
      <li>Neil Borromi, O.D.</li>
    </ul>

    <address class="contact">
      417 Pembrook Parkway<br>
      Brantwell Harbor, Vermont 05871<br>
      516-902-4471
    </address>
  </main>
</body>
</html>
```